Author book covers needed for a spiritual book, eastern wisdom

I need a cover for a 'Anthology'. I'm an author and I have established myself in a genre of its own, a symbiosis between spirituality and literature. My books are always a mix of entertainment and depth. Many of my readers have highlighted in the now eight books I have written many passages and asked me if it was not possible to collect all the wisdom, quotes, sayings and stories in a volume of aphorisms. I did this. Worker Title: "Lantern of quiet rain ... to let your days find their way home" Seeking a cover that this gold dust elements and at the same time combines the possibility of transformation and a bit mystical. .. Mainly it's in my books to eastern philosophies, ie Buddhism, Upanishads, the Vedas ... the Yoga Vasishta, the Bhagavad Gita and the like A variable template I found at plimvoro - but it is not a must, if anyone has a better has idea. Be creative! My author name: Marela Tovanni greetings Marela Tovanni

Target Market(s)

People who are spiritually interested and concerned about their lives make the book to be traded as a gift - and thus look accordingly.

Requirements
Must have
• a spiritual touch - spiritual touch if possible - a gift-character, so did customers feel inspired to give the book as a present to friends and relatives or other people. Please place the author's name at the lower end.
Nice to have
• Gold particles and Luminiscence ... to express did the word inside the book hopefully lighten up ones heart, to illumine ones soul or to help through a critical situation. So to say, bring some gold into a dark world ...
Should not have
• pls no black cover

```html
<!DOCTYPE html>
<html lang="en">
<head>
<meta charset="utf-8">
<title>Lantern of Quiet Rain — Marela Tovanni</title>
<link rel="stylesheet" href="https://fonts.googleapis.com/css2?family=Cinzel:wght@500;600&family=Josefin+Sans:wght@300;400&display=swap">
<style>
  :root {
    --stage: #d9d9d9;
    --umber-deep: #1c0c06;
    --umber: #3b2211;
    --bronze: #6e4220;
    --gold: #e9b850;
    --gold-light: #fbe7a6;
    --glow: #fff4c9;
    --title-ink: #6a3512;
    --subtitle-ink: #4a2a12;
    --author-ink: #f4eaa4;
  }
  * { box-sizing: border-box; margin: 0; padding: 0; }
  html, body {
    width: 1200px;
    height: 1200px;
    overflow: hidden;
  }
  body {
    background: radial-gradient(ellipse at 50% 45%, #ededed 0%, var(--stage) 70%);
    position: relative;
  }
  .cover {
    position: absolute;
    left: 254px;
    top: 60px;
    width: 692px;
    height: 1080px;
    overflow: hidden;
    background:
      linear-gradient(180deg, var(--umber) 0%, #6a4420 22%, #b68a45 45%, #8a5528 58%, #3e1b0c 72%, var(--umber-deep) 100%);
  }
  .cover__artwork {
    position: absolute;
    inset: 0;
    background:
      radial-gradient(ellipse 34% 26% at 57% 44%, var(--glow) 0%, rgba(251, 231, 166, 0.85) 35%, rgba(233, 184, 80, 0.35) 70%, rgba(233, 184, 80, 0) 100%),
      radial-gradient(ellipse 70% 45% at 55% 42%, rgba(233, 184, 80, 0.55) 0%, rgba(233, 184, 80, 0) 75%),
      linear-gradient(180deg, rgba(0,0,0,0) 60%, rgba(60, 20, 8, 0.6) 64%, rgba(28, 12, 6, 0.95) 80%);
  }
  .cover__ring {
    position: absolute;
    left: 60px;
    top: 150px;
    width: 600px;
    height: 600px;
  }
  .cover__title {
    position: absolute;
    left: 0;
    right: 0;
    top: 255px;
    text-align: center;
    font-family: "Cinzel", serif;
    font-weight: 600;
    font-size: 74px;
    line-height: 0.98;
    letter-spacing: -1px;
    color: var(--title-ink);
    text-shadow: 0 0 6px rgba(255, 240, 190, 0.6);
  }
  .cover__subtitle {
    position: absolute;
    left: 0;
    right: 0;
    top: 423px;
    text-align: center;
    font-family: "Josefin Sans", sans-serif;
    font-weight: 400;
    font-size: 21px;
    letter-spacing: 0.5px;
    color: var(--subtitle-ink);
  }
  .cover__author {
    position: absolute;
    left: 0;
    right: 0;
    top: 800px;
    text-align: center;
    font-family: "Josefin Sans", sans-serif;
    font-weight: 300;
    font-size: 104px;
    line-height: 1.02;
    letter-spacing: 9px;
    color: var(--author-ink);
  }
</style>
</head>
<body>
  <main class="cover">
    <div class="cover__artwork" role="img" aria-label="Golden glowing backdrop with a kneeling winged figure with large translucent butterfly wings on a dark rippled ground, scattered with gold dust"></div>
    <svg class="cover__ring" viewBox="0 0 600 600" aria-hidden="true">
      <defs>
        <linearGradient id="ring-gold" x1="0" y1="0" x2="1" y2="1">
          <stop offset="0" stop-color="#fff4c9"/>
          <stop offset="0.5" stop-color="#e9b850"/>
          <stop offset="1" stop-color="#fff4c9"/>
        </linearGradient>
      </defs>
      <path d="M 150 70 A 270 270 0 0 0 300 570" fill="none" stroke="url(#ring-gold)" stroke-width="7" stroke-linecap="round" opacity="0.9"/>
      <path d="M 540 380 A 270 270 0 0 1 330 568" fill="none" stroke="url(#ring-gold)" stroke-width="6" stroke-linecap="round" opacity="0.85"/>
    </svg>
    <h1 class="cover__title">LANTERN OF<br>QUIET RAIN...</h1>
    <p class="cover__subtitle">TO LET YOUR DAYS FIND THEIR WAY HOME</p>
    <p class="cover__author">MARELA<br>TOVANNI</p>
  </main>
</body>
</html>
```